Harbourline construction company Business card design

I need a business card design for my company. I have a logo but dont have business cards with our logo..

www.harbourlineconstructco.com.au

The logo is on the website

I need the same details as this design I have attached. we have changed the logo and colours. just like the website

Industry/Entity Type

Building

```html
<!DOCTYPE html>
<html lang="en">
<head>
<meta charset="utf-8">
<title>Harbourline Construction – Business Card</title>
<link rel="stylesheet" href="https://fonts.googleapis.com/css2?family=Arimo:wght@400;700&family=Tinos:wght@400;700&display=swap">
<style>
  :root {
    --brand-blue: #2a8cd0;
    --ink: #1a1a1a;
    --text-grey: #333333;
    --divider: #4a4a4a;
    --band-black: #0a0a0a;
    --paper: #ffffff;
  }
  * { margin: 0; padding: 0; box-sizing: border-box; }
  html, body { width: 1200px; height: 705px; overflow: hidden; background: var(--paper); }
  .card {
    position: relative;
    width: 1200px;
    height: 705px;
    background: var(--paper);
    font-family: "Arimo", Arial, sans-serif;
    color: var(--ink);
  }
  .brand-square {
    position: absolute;
    left: 206px;
    top: 90px;
    width: 200px;
    height: 200px;
    background: var(--brand-blue);
  }
  .brand-name {
    position: absolute;
    left: 96px;
    top: 378px;
    width: 420px;
    text-align: center;
    font-family: "Arimo", Arial, sans-serif;
    font-weight: 700;
    font-size: 31px;
    color: var(--brand-blue);
    white-space: nowrap;
  }
  .brand-rule {
    position: absolute;
    left: 106px;
    top: 505px;
    width: 400px;
    height: 2px;
    background: var(--divider);
  }
  .services {
    position: absolute;
    left: 96px;
    top: 528px;
    width: 420px;
    text-align: center;
    font-family: "Tinos", "Times New Roman", serif;
    font-size: 20px;
    line-height: 33px;
    color: var(--ink);
    white-space: nowrap;
  }
  .divider {
    position: absolute;
    left: 597px;
    top: 108px;
    width: 3px;
    height: 466px;
    background: var(--divider);
  }
  .person {
    position: absolute;
    left: 717px;
    top: 108px;
    width: 420px;
  }
  .person-name {
    font-family: "Tinos", "Times New Roman", serif;
    font-size: 50px;
    font-weight: 400;
    letter-spacing: 1px;
    color: var(--ink);
    line-height: 1;
    white-space: nowrap;
  }
  .person-role {
    text-align: right;
    font-size: 31px;
    color: var(--brand-blue);
    margin-top: 6px;
  }
  .contacts {
    position: absolute;
    left: 676px;
    top: 300px;
    list-style: none;
  }
  .contacts li {
    display: flex;
    align-items: center;
    height: 65px;
    font-size: 31px;
    color: var(--text-grey);
    white-space: nowrap;
  }
  .contacts li.email { font-size: 25px; }
  .contacts svg { width: 30px; height: 30px; margin-right: 18px; fill: var(--brand-blue); flex: none; }
  .band-black {
    position: absolute;
    left: 0; top: 636px;
    width: 1200px; height: 43px;
    background: var(--band-black);
  }
  .reg-no {
    position: absolute;
    right: 40px; top: 646px;
    font-size: 21px;
    font-weight: 700;
    color: var(--paper);
  }
  .band-blue {
    position: absolute;
    left: 0; top: 679px;
    width: 1200px; height: 26px;
    background: var(--brand-blue);
  }
</style>
</head>
<body>
<div class="card">
  <div class="brand-square" aria-hidden="true"></div>
  <p class="brand-name">Harbourline Construction</p>
  <div class="brand-rule"></div>
  <p class="services">New Homes • Additions &amp; Renovations<br>Domestic &amp; Commerical Builders</p>

  <div class="divider"></div>

  <div class="person">
    <h1 class="person-name">PETRA VALEK</h1>
    <p class="person-role">Director</p>
  </div>

  <ul class="contacts">
    <li>
      <svg viewBox="0 0 24 24" aria-hidden="true"><path d="M6.6 10.8a15.1 15.1 0 0 0 6.6 6.6l2.2-2.2c.3-.3.7-.4 1-.2 1.1.4 2.3.6 3.6.6.6 0 1 .4 1 1V20c0 .6-.4 1-1 1A17 17 0 0 1 3 4c0-.6.4-1 1-1h3.5c.6 0 1 .4 1 1 0 1.3.2 2.5.6 3.6.1.3 0 .7-.2 1z"/></svg>
      08 9410 5836
    </li>
    <li>
      <svg viewBox="0 0 24 24" aria-hidden="true"><path d="M8 2h8a2 2 0 0 1 2 2v16a2 2 0 0 1-2 2H8a2 2 0 0 1-2-2V4a2 2 0 0 1 2-2zm0 3v12h8V5zm4 13.5a1 1 0 1 0 0 2 1 1 0 0 0 0-2z"/></svg>
      08 9410 5836
    </li>
    <li>
      <svg viewBox="0 0 24 24" aria-hidden="true"><path d="M3 7h3V3h10l3 3v1h2a1 1 0 0 1 1 1v11a1 1 0 0 1-1 1H3a1 1 0 0 1-1-1V8a1 1 0 0 1 1-1zm5-2v5h9V7h-3V5zm6 8v2h2v-2zm-4 0v2h2v-2zm4 3v2h2v-2zm-4 0v2h2v-2z"/></svg>
      0412 580 264
    </li>
    <li class="email">
      <svg viewBox="0 0 24 24" aria-hidden="true"><path d="M3 5h18a1 1 0 0 1 1 1v12a1 1 0 0 1-1 1H3a1 1 0 0 1-1-1V6a1 1 0 0 1 1-1zm1 2.2V17h16V7.2l-8 5.3z M4.6 7 12 11.9 19.4 7z"/></svg>
      office@harbourlineconstructco.com.au
    </li>
  </ul>

  <div class="band-black"></div>
  <p class="reg-no">Reg. No. 20583</p>
  <div class="band-blue"></div>
</div>
</body>
</html>
```